Post card design for ( Interior ) & ( Exterior ) Residential Painting

We need a post card design for interior painting. To get homeowners to call about getting there interior home painted before the end winter comes, to get a clean, quality and no hassle paint job with low odor paints

Some IDEAS:
Exterior Paint Season is Coming to Northern VA and Metro DC!
Have you taken a look around your house this winter? Have you noticed any areas of unwanted moisture, mold or draft? Keeping your house painted and well-maintained on the outside will save money in the future as well. It protects your home from the elements – whether, wind, rain and snow or the strong summer sun.

idea #2
Exterior Paint Makes Your House Last Longer
aintaining a good coat of the correct type of paint on the exterior of your home will help protect your home from the elements and extend the overall life of the structure
idea #3
Rotten Wood and Two Other TOP Reasons for Exterior Paint
We’ll start there – rotten wood – the first reason for exterior paint. If your home or building has decorative wood trim, wood siding or even wood around windows and doors, it could be at risk for rotten or rotting wood. Maintaining a healthy and COMPLETE coat of paint will protect the wood from water damage. Additionally, during a paint project, our team can assess wooden areas and advise if there are any places of concern. For a long-term solution, consider replacing wood trim with vinyl or wood alternatives that stand up to the elements. This can also be done during an exterior paint project.
Idea # 4
Benefits of Using Low-VOC interior Paints
Paints with low-VOC or Zero-VOC are considered healthier options due to the lower amount of toxins they release when applied to a wall. Latex paints are popular low-VOC because they are water based and don’t contain other chemicals you may find in oil-based paints.

Less odor! Because these paints have lower levels of toxins that are released, the paint smell that is associated with a fresh coat of paint is not as strong. Low-VOC would be a great option if you plan on painting a nursery because the smell won’t linger. Although you might not smell it, it is always important to ventilate the room. All paints, even low-VOC have levels of toxicity which are not good to breathe in for long periods of time.

Target Market(s)

single family homes

Colors

Designer to choose colors to be used in the design.

Requirements
Should not have
• cheep, free

```html
<!DOCTYPE html>
<html lang="en">
<head>
<meta charset="utf-8">
<title>Crest Painting – Exterior Paint Season Postcard</title>
<link rel="stylesheet" href="https://fonts.googleapis.com/css2?family=Bebas+Neue&family=Roboto:wght@400;700&display=swap">
<style>
  :root {
    --brand-red: #e31c3d;
    --deep-red: #8c1a1f;
    --ink: #161616;
    --paper: #ffffff;
    --photo-stone: #b9b6ae;
    --photo-brick: #7d5a4f;
    --photo-leaf: #5d7a3c;
    --photo-sky: #e8ecef;
  }
  html, body {
    margin: 0;
    padding: 0;
    width: 1200px;
    height: 816px;
    overflow: hidden;
    background: var(--paper);
  }
  .postcard {
    position: relative;
    width: 1200px;
    height: 816px;
    overflow: hidden;
    background: var(--paper);
    font-family: "Roboto", Arial, sans-serif;
    color: var(--ink);
  }
  .postcard__art {
    position: absolute;
    inset: 0;
    width: 1200px;
    height: 816px;
  }
  .brand {
    position: absolute;
    left: 62px;
    top: 170px;
    display: flex;
    align-items: center;
    gap: 18px;
  }
  .brand__mark {
    width: 34px;
    height: 34px;
    background: var(--brand-red);
  }
  .brand__name {
    margin: 0;
    font-family: "Bebas Neue", Impact, sans-serif;
    font-weight: 400;
    font-size: 78px;
    line-height: 0.86;
    color: var(--ink);
  }
  .headline {
    position: absolute;
    left: 62px;
    top: 381px;
    margin: 0;
    font-family: "Bebas Neue", Impact, sans-serif;
    font-weight: 400;
    font-size: 64px;
    line-height: 60px;
    letter-spacing: 1.6px;
    color: var(--ink);
  }
  .headline__accent { color: var(--brand-red); }
  .pitch {
    position: absolute;
    left: 62px;
    top: 648px;
    width: 1080px;
  }
  .pitch__question {
    margin: 0 0 8px;
    font-size: 22px;
    font-weight: 700;
    color: var(--brand-red);
  }
  .pitch__body {
    margin: 0;
    font-size: 19.5px;
    line-height: 25.5px;
    color: var(--ink);
  }
  .footer-rules {
    position: absolute;
    left: 0;
    top: 770px;
    width: 1200px;
  }
  .footer-rules__line {
    width: 100%;
    background: var(--brand-red);
  }
  .footer-rules__line--thick { height: 4px; margin-bottom: 11px; }
  .footer-rules__line--thin { height: 2px; margin-bottom: 12px; }
</style>
</head>
<body>
<main class="postcard">
  <svg class="postcard__art" viewBox="0 0 1200 816" xmlns="http://www.w3.org/2000/svg">
    <defs>
      <linearGradient id="townhouse-tones" x1="0" y1="0" x2="1" y2="1">
        <stop offset="0" stop-color="var(--photo-sky)"/>
        <stop offset="0.3" stop-color="var(--photo-stone)"/>
        <stop offset="0.6" stop-color="var(--photo-brick)"/>
        <stop offset="0.9" stop-color="var(--photo-leaf)"/>
      </linearGradient>
    </defs>
    <polygon class="hero-photo" role="img"
      aria-label="Photo of a row of Victorian townhouses in brick and painted stone with green trees and front gardens"
      points="560,0 1200,0 1200,620 760,620" fill="url(#townhouse-tones)"/>
    <polygon class="edge-band" points="505,0 545,0 745,620 705,620" fill="var(--brand-red)"/>
  </svg>

  <div class="brand">
    <span class="brand__mark"></span>
    <p class="brand__name">Crest<br>Painting</p>
  </div>

  <h1 class="headline">
    <span class="headline__accent">Exterior Paint</span> Season<br>
    Is Coming to Northern<br>
    <span class="headline__accent">VA and Metro DC!</span>
  </h1>

  <section class="pitch">
    <h2 class="pitch__question">Have you taken a look around your house this winter?</h2>
    <p class="pitch__body">Have you noticed any areas of unwanted moisture, mold or draft? Keeping your house painted and well-maintained on the outside will save money in the future as well. It protects your home from the elements – whether, wind, rain and snow or the strong summer sun.</p>
  </section>

  <div class="footer-rules">
    <div class="footer-rules__line footer-rules__line--thick"></div>
    <div class="footer-rules__line footer-rules__line--thin"></div>
    <div class="footer-rules__line footer-rules__line--thin"></div>
  </div>
</main>
</body>
</html>
```